Letterhead

We have a new logo and would like to design electronic letterhead with our new logo. We have two office locations. One of our offices is moving in July.

```html
<!DOCTYPE html>
<html lang="en">
<head>
<meta charset="utf-8">
<title>Letterhead – Harlow Brennan Lisle Ostrander</title>
<link href="https://fonts.googleapis.com/css2?family=Montserrat:wght@400;600&family=PT+Sans:wght@400&family=Arimo:wght@700&display=swap" rel="stylesheet">
<style>
  :root {
    --backdrop: #e3e4e5;
    --paper: #f8f8f8;
    --ink: #2b2b2b;
    --body-ink: #3a3a3a;
    --brand-blue: #2566b0;
    --brand-navy: #1c2236;
    --footer-text: #ffffff;
  }
  * { box-sizing: border-box; margin: 0; padding: 0; }
  html, body { width: 1200px; height: 945px; overflow: hidden; background: var(--backdrop); }
  .canvas { position: relative; width: 1200px; height: 945px; }
  .letterhead {
    position: absolute; left: 282px; top: 22px;
    width: 636px; height: 900px;
    background: var(--paper);
    box-shadow: 0 6px 18px rgba(0,0,0,.12);
    overflow: hidden;
  }
  .firm-mark {
    position: absolute; top: 46px; left: 0; width: 100%;
    text-align: center;
  }
  .firm-name {
    font-family: "Montserrat", sans-serif; font-weight: 600;
    font-size: 15px; line-height: 15px; letter-spacing: 1.5px;
    color: var(--ink); text-transform: uppercase;
  }
  .firm-tagline {
    margin-top: 3px;
    font-family: "Montserrat", sans-serif; font-weight: 400;
    font-size: 11px; letter-spacing: 2.4px;
    color: var(--brand-blue); text-transform: uppercase;
  }
  .letter-body {
    position: absolute; top: 190px; left: 70px; right: 70px;
    font-family: "PT Sans", sans-serif;
    font-size: 12.5px; line-height: 15.5px; color: var(--body-ink);
  }
  .salutation {
    font-family: "Arimo", sans-serif; font-weight: 700;
    font-size: 14px; color: #1a1a1a; margin-bottom: 14px;
  }
  .letter-body p { text-indent: 18px; margin-bottom: 15px; text-align: justify; }
  .signature {
    position: absolute; top: 640px; left: 78px;
    width: 120px; height: 40px; border-radius: 4px;
    background: linear-gradient(90deg, #d9d9d9, #ececec);
  }
  .footer-band { position: absolute; left: 0; bottom: 0; width: 636px; height: 150px; }
  .footer-contact {
    position: absolute; right: 28px; bottom: 22px;
    font-family: "Montserrat", sans-serif; font-size: 10.5px; line-height: 17px;
    color: var(--footer-text); text-align: right;
  }
  .footer-contact svg { vertical-align: -1px; margin-right: 3px; }
</style>
</head>
<body>
<div class="canvas">
  <article class="letterhead">
    <header class="firm-mark">
      <div class="firm-name">Harlow Brennan<br>Lisle Ostrander</div>
      <div class="firm-tagline">Attorneys at Law</div>
    </header>

    <section class="letter-body">
      <div class="salutation">Dear Mr. John,</div>
      <p>Lorem Ipsum is simply dummy text of the printing and typesetting industry. Lorem Ipsum has been the industry's standard dummy text ever since the 1500s, when an unknown printer took a galley of type and scrambled it to make a type specimen book. It has survived not only five centuries, but also the leap into electronic typesetting, remaining essentially unchanged.</p>
      <p>The standard chunk of Lorem Ipsum used since the 1500s is reproduced below for those interested. Sections 1.10.32 and 1.10.33 from "de Ordine Verborum Antiquo" by Varenius are also reproduced in their exact original form, accompanied by English versions from the 1914 translation by L. Marden</p>
      <p>Lorem Ipsum is simply dummy text of the printing and typesetting industry. Lorem Ipsum has been the industry's standard dummy text ever since the 1500s, when an unknown printer took a galley of type and scrambled it to make a type specimen book. It has survived not only five centuries, but also the leap into electronic typesetting, remaining essentially unchanged. It was popularised in the</p>
      <p>The standard chunk of Lorem Ipsum used since the 1500s is reproduced below for those interested. Sections 1.10.32 and 1.10.33 from "de Ordine Verborum Antiquo" by Varenius are also reproduced in their exact original form, accompanied by English versions from the 1914 translation by L. Marden</p>
      <p>The standard chunk of Lorem Ipsum used since the 1500s is reproduced below for those interested. Sections 1.10.32 and 1.10.33 from "de Ordine Verborum Antiquo" by Varenius are also reproduced in their exact original form.</p>
    </section>

    <div class="signature" role="img" aria-label="Handwritten signature"></div>

    <svg class="footer-band" viewBox="0 0 636 150" preserveAspectRatio="none" aria-hidden="true">
      <path d="M0,150 Q300,60 636,0 L636,150 Z" fill="var(--brand-blue)"/>
      <path d="M0,148 Q300,52 636,-6 L636,-2 Q300,58 0,150 Z" fill="var(--brand-navy)"/>
    </svg>
    <footer class="footer-contact">
      <div>PO Box 418, 27 Kestrel Lane, Brookvale - 41700</div>
      <div>
        <svg width="9" height="9" viewBox="0 0 10 10"><path d="M2 0.5 L4 3 L3 4.2 Q4.3 6 5.8 7 L7 6 L9.5 8 L8.2 9.6 Q3.5 9 0.5 2 Z" fill="#fff"/></svg>+61 7 555 0142
        &nbsp;<svg width="9" height="9" viewBox="0 0 10 10"><rect x="0.5" y="1.5" width="9" height="7" rx="1" fill="none" stroke="#fff"/><path d="M0.8 2 L5 5.5 L9.2 2" fill="none" stroke="#fff"/></svg>info@harlowbrennan.com
        &nbsp;<svg width="9" height="9" viewBox="0 0 10 10"><circle cx="5" cy="5" r="4.5" fill="#fff"/></svg>www.harlowbrennan.com
      </div>
    </footer>
  </article>
</div>
</body>
</html>
```